Plenq - Shoe Fitting App : Foot scanning app, 3D reconstruction and Fit recommandation.

We are a startup that has developed a 3D scanning App that compares the 3d reconstructed foot to the 3D Last (mould) of a shoe to find the best match and recommend a shoe size with a graphical representation of the fit on a reconstructed foot without texturing. The challenge of this app is to have a simple and intuitive onboarding of the user with clean and crisp ui and a simple tutorial for foot scanning. 3D representation of the fit is also key. What you see is what you feel is what we would like to achieve.

Target Market(s)

Sneaker Brands and athletic shoes brands

Industry/Entity Type

Footwear

Font styles to use
Other font styles liked:
• Oswald or Droid Serif

Colors
0094D4
00A9DD
6FCCEA
C7EBF8
E9F6FB

Requirements
Must have
• Simple intuitive UI to onboard the customer to scan his bare foot (please look at attached image on how to scan the foot). You must flip your phone so that the screen is facing your foot. Start at 40cm distance form the front of your foot and turn 360% slowly to capture the foot while you feel the aptic of the iPhone. That needs to be presented with a simple animation that the user can easily understand and skip if he is a returning customer and knows how to do that. the rest of the UI is to present the result of the scanned foot for the user to use to get his fit and size. The other must have is the final result screen. Where the user will a representation of the foot (snug, loose ) of different predefined areas of the foot so he can choose the fit that he likes and not necessarily the size that we suggest. Must match website design (https://www.plenq-example.ai)
Nice to have
• An animation of the whole process (scan-compare 3d foot with 3d shoe last(or mould) and get the 3D result of the best fit + associated size. Optionaly, an option to play with your foot and transform it (avatar like with accessories and colours)
Should not have
• Too many colours. Too much text. No gender type. No race type.

```html
<!DOCTYPE html>
<html lang="en">
<head>
<meta charset="utf-8">
<title>Plenq – Foot Scan Onboarding</title>
<link href="https://fonts.googleapis.com/css2?family=Poppins:ital,wght@0,400;0,500;0,600;0,700;1,400&display=swap" rel="stylesheet">
<style>
  :root{
    --bg-top:#0a0a0a;
    --bg-bottom:#5c5c5c;
    --panel-top:#3b3b3b;
    --panel-bottom:#000000;
    --text:#ffffff;
    --text-soft:#e6e6e6;
    --line:#6a6a6a;
    --card:#1e1e1e;
    --pill:#3a3a3a;
    --track:#1a1a1a;
  }
  *{box-sizing:border-box;margin:0;padding:0}
  html,body{width:1200px;height:650px;overflow:hidden}
  body{
    background:linear-gradient(180deg,var(--bg-top) 0%,var(--bg-bottom) 100%);
    font-family:"Poppins",sans-serif;color:var(--text);position:relative;
  }
  .screen{
    position:absolute;top:24px;width:278px;height:603px;overflow:hidden;
    background:linear-gradient(180deg,var(--panel-top) 0%,#202020 45%,var(--panel-bottom) 80%);
  }
  .screen--1{left:21px}.screen--2{left:316px}.screen--3{left:610px}.screen--4{left:904px}
  .brand{position:absolute;left:20px;top:24px;font-size:20px;font-weight:700;letter-spacing:.5px;line-height:26px}
  .menu{position:absolute;right:19px;top:30px;width:3px;display:flex;flex-direction:column;gap:3px}
  .menu span{width:3px;height:3px;border-radius:50%;background:var(--text)}
  .headline{position:absolute;left:0;right:0;text-align:center;font-weight:400;font-size:23px;line-height:28.5px}
  .headline strong{font-weight:700}
  .headline--lit{top:92px}
  .headline--shoes{top:70px}
  .body-copy{position:absolute;left:36px;right:36px;top:164px;text-align:center;font-size:9px;line-height:14.3px;color:var(--text-soft)}
  .visual{
    position:absolute;left:0;right:0;top:241px;height:232px;border-radius:36px;
    background:radial-gradient(ellipse at 50% 40%,#ffffff 0%,#c8c8c8 45%,#1a1a1a 100%);
  }
  .visual--shoes{background:radial-gradient(ellipse at 50% 55%,#f2b46a 0%,#b8477a 22%,#d8d8d8 40%,#8c8c8c 70%,#1a1a1a 100%)}
  .visual--feet{background:radial-gradient(ellipse at 50% 50%,#f6a871 0%,#f6a871 20%,#c9c9c9 42%,#7a7a7a 72%,#1a1a1a 100%)}
  .btn{
    position:absolute;top:511px;height:46px;border-radius:23px;display:flex;align-items:center;justify-content:center;
    font-size:15px;font-weight:500;border:1px solid #5a5a5a;
    background:linear-gradient(180deg,#3e3e3e,#2a2a2a);color:var(--text);
  }
  .btn--skip{left:19px;width:182px}
  .btn--wide{left:47px;width:183px}
  .btn--light{background:#ffffff;color:#111;border-color:#ffffff}
  .btn--next{left:211px;width:45px;height:45px;border-radius:50%;background:#fff;border-color:#fff}
  .hint-box{
    position:absolute;left:19px;right:21px;top:85px;height:49px;border:1px solid var(--line);border-radius:6px;
    background:#2b2b2b;display:flex;align-items:center;justify-content:center;text-align:center;font-size:8.5px;line-height:13px;padding:0 40px
  }
  .turn-ring{position:absolute;left:25px;top:179px;width:60px;height:60px}
  .turn-ring span{position:absolute;inset:0;display:flex;align-items:center;justify-content:center;font-size:14px;font-weight:500}
  .stage{position:absolute;left:0;top:240px;width:278px;height:220px}
  .foot-model{
    position:absolute;left:70px;top:16px;width:125px;height:170px;border-radius:40px 40px 60px 60px;
    background:radial-gradient(ellipse at 60% 70%,#9a9a9a 0%,#555 45%,rgba(30,30,30,0) 75%)
  }
  .rotate-pill{
    position:absolute;left:122px;top:432px;width:38px;height:23px;border-radius:12px;border:1px solid #bdbdbd;background:#2a2a2a;
    display:flex;align-items:center;justify-content:center;gap:6px
  }
  .card{position:absolute;left:19px;right:21px;border:1px solid var(--line);border-radius:6px;background:var(--card);text-align:center}
  .card h3{font-size:13px;font-weight:400;line-height:18px}
  .card p{font-size:8.5px;line-height:13px;color:var(--text-soft)}
  .card--loading{top:91px;height:84px;padding-top:14px}
  .card--loading p{margin-top:3px}
  .progress{position:absolute;left:17px;right:18px;top:56px;height:10px;border-radius:5px;background:var(--track);border:1px solid #2e2e2e}
  .progress span{display:block;width:36%;height:100%;border-radius:5px;background:#fff}
  .card--facts{top:190px;height:74px;padding-top:14px}
  .card--facts p{font-style:italic;margin-top:4px;padding:0 18px}
  .card--pref{top:279px;height:145px;padding-top:14px}
  .card--pref h3{margin-bottom:3px}
  .options{display:flex;justify-content:center;gap:7px;margin-top:12px}
  .option{height:24px;border-radius:12px;border:1px solid #6a6a6a;background:var(--pill);font-size:10.5px;display:flex;align-items:center;justify-content:center}
  .option--soft{width:52px}.option--medium{width:67px;background:#111;border-color:#fff;color:#fff}.option--hard{width:51px}
  .card--pref .note{margin-top:14px;padding:0 20px}
</style>
</head>
<body>

<section class="screen screen--1">
  <div class="brand">PLENQ</div>
  <div class="menu"><span></span><span></span><span></span></div>
  <h1 class="headline headline--lit">Make sure you're<br>in a <strong>well-lit area</strong></h1>
  <p class="body-copy">Avoid strong light from only one direction. This casts deep shadows that reduce the accuracy of the scan.</p>
  <div class="visual visual--shoes" role="img" aria-label="Illustration of legs in rolled jeans wearing colourful sneakers"></div>
  <div class="btn btn--skip">Skip Intro</div>
  <div class="btn btn--next">
    <svg width="24" height="14" viewBox="0 0 24 14"><path d="M1 7h3M7 7h14M15 1l6 6-6 6" fill="none" stroke="#111" stroke-width="1.6" stroke-linecap="round" stroke-linejoin="round"/></svg>
  </div>
</section>

<section class="screen screen--2">
  <div class="brand">PLENQ</div>
  <div class="menu"><span></span><span></span><span></span></div>
  <h1 class="headline headline--shoes">Take off your<br>shoes and <strong>roll up<br>pants</strong></h1>
  <p class="body-copy">To scan your feet, the camera needs to see the unique details, including your ankle</p>
  <div class="visual visual--feet" role="img" aria-label="Illustration of bare feet with rolled up trouser legs"></div>
  <div class="btn btn--skip">Skip Intro</div>
  <div class="btn btn--next">
    <svg width="24" height="14" viewBox="0 0 24 14"><path d="M1 7h3M7 7h14M15 1l6 6-6 6" fill="none" stroke="#111" stroke-width="1.6" stroke-linecap="round" stroke-linejoin="round"/></svg>
  </div>
</section>

<section class="screen screen--3">
  <div class="brand">PLENQ</div>
  <div class="menu"><span></span><span></span><span></span></div>
  <div class="hint-box">Flip the screen towards your toes to start scanning</div>
  <div class="turn-ring">
    <svg width="60" height="60" viewBox="0 0 60 60"><circle cx="30" cy="30" r="28" fill="none" stroke="#6a6a6a" stroke-width="2.5"/><circle cx="28" cy="2" r="2" fill="#fff"/></svg>
    <span>360°</span>
  </div>
  <div class="stage">
    <svg width="278" height="220" viewBox="0 0 278 220"><ellipse cx="137" cy="159" rx="116" ry="44" fill="none" stroke="#bdbdbd" stroke-width="2"/></svg>
    <div class="foot-model" role="img" aria-label="3D wireframe model of a scanned foot standing on the platform"></div>
  </div>
  <div class="rotate-pill">
    <svg width="6" height="10" viewBox="0 0 6 10"><path d="M5 1 1 5l4 4" fill="none" stroke="#fff" stroke-width="1.2"/></svg>
    <svg width="6" height="10" viewBox="0 0 6 10"><path d="M1 1l4 4-4 4" fill="none" stroke="#fff" stroke-width="1.2"/></svg>
  </div>
  <div class="btn btn--wide">Right Foot</div>
</section>

<section class="screen screen--4">
  <div class="brand">PLENQ</div>
  <div class="menu"><span></span><span></span><span></span></div>
  <div class="card card--loading">
    <h3>Loading your data</h3>
    <p>This process might take a few minutes</p>
    <div class="progress"><span></span></div>
  </div>
  <div class="card card--facts">
    <h3>Fun Facts About Feet</h3>
    <p>Our feet have nearly a quarter of all the bones in our bodies–each one has 26 bones</p>
  </div>
  <div class="card card--pref">
    <h3>Tell us your preference</h3>
    <p>How do you prefer the cushion?</p>
    <div class="options">
      <div class="option option--soft">Soft</div>
      <div class="option option--medium">Medium</div>
      <div class="option option--hard">Hard</div>
    </div>
    <p class="note">Select an option to go to the next personal preference setting</p>
  </div>
  <div class="btn btn--wide btn--light">See Result</div>
</section>

</body>
</html>
```